Real estate investor, needing a business card that communicates warmth, integrity, empathy.

I have a logo that can be manipulated to align with the message - "Serving your home selling needs." Want it to stand out from typical real estate investor cards, and make distressed home sellers feel a connection with me. Should communicate warmth, integrity, empathy, and trustworthiness.

Target Market(s)

Distressed home owners who need to sell their homes, not using realtors.

Contact Information for Business Card

Glossy front and matte back, with a small box that is labelled "notes." I like darker blues and blacks together, but doesn't have to be, as long as it communicates trustworthiness, and a strong call to action.

Other font styles liked:
• see "must haves" above, but willing to review whatever comes my way.

Requirements
Must have
• The fonts on my logo are Aviano, Lusitana, and Marcellus. We don't have to use those, but I favor them.

```html
<!DOCTYPE html>
<html lang="en">
<head>
<meta charset="utf-8">
<title>Ravi Menon – Business Card</title>
<link rel="stylesheet" href="https://fonts.googleapis.com/css2?family=Open+Sans:wght@400;600;700&family=League+Spartan:wght@700&display=swap">
<style>
  :root {
    --backdrop: #dedede;
    --card: #ffffff;
    --bronze: #a67948;
    --ink: #1a1a1a;
    --text: #2b2b2b;
    --photo-light: #f6f7f7;
    --photo-mid: #e9eeec;
  }
  * { margin: 0; padding: 0; box-sizing: border-box; }
  html, body {
    width: 1200px;
    height: 800px;
    overflow: hidden;
    background: var(--backdrop);
    font-family: "Open Sans", Arial, sans-serif;
  }
  .card {
    position: absolute;
    width: 381px;
    height: 636px;
    background: var(--card);
    overflow: hidden;
  }
  .card--front { left: 134px; top: 63px; }
  .card--back { left: 600px; top: 61px; }

  .card__shapes {
    position: absolute;
    inset: 0;
    width: 381px;
    height: 636px;
  }

  /* Front */
  .agent-name {
    position: absolute;
    left: 64px;
    top: 64px;
    font-size: 35px;
    line-height: 40px;
    letter-spacing: 0.5px;
    white-space: nowrap;
  }
  .agent-name__first { font-weight: 700; color: var(--ink); }
  .agent-name__last { font-weight: 600; color: var(--bronze); }
  .agent-role {
    position: absolute;
    left: 64px;
    top: 100px;
    font-size: 16px;
    font-weight: 600;
    color: var(--ink);
  }
  .contact-rail {
    position: absolute;
    left: 64px;
    top: 158px;
    width: 21px;
    height: 74px;
    border-radius: 11px;
    background: var(--bronze);
  }
  .contact-icon {
    position: absolute;
    left: 4px;
    width: 13px;
    height: 13px;
  }
  .contact-list {
    position: absolute;
    left: 92px;
    top: 158px;
    list-style: none;
    font-size: 16px;
    color: var(--text);
  }
  .contact-list li { height: 24px; line-height: 24px; white-space: nowrap; }

  .brand-name {
    position: absolute;
    font-family: "Open Sans", Arial, sans-serif;
    font-weight: 700;
    color: var(--ink);
    letter-spacing: 10px;
    text-align: center;
    white-space: nowrap;
  }
  .card--front .brand-name {
    left: 0;
    width: 381px;
    top: 402px;
    font-size: 20px;
    padding-left: 10px;
  }
  .card--back .brand-name {
    left: 0;
    width: 381px;
    top: 112px;
    font-size: 28px;
    padding-left: 20px;
  }

  /* Back */
  .tagline {
    position: absolute;
    left: 75px;
    top: 452px;
    font-family: "League Spartan", "Open Sans", sans-serif;
    font-weight: 700;
    font-size: 33px;
    line-height: 38px;
    color: #ffffff;
    text-transform: uppercase;
    letter-spacing: -0.3px;
  }
</style>
</head>
<body>

<section class="card card--front" aria-label="Business card front">
  <svg class="card__shapes" viewBox="0 0 381 636" aria-hidden="false">
    <defs>
      <linearGradient id="photoTone" x1="0" y1="0" x2="0" y2="1">
        <stop offset="0" stop-color="#eef2f1"/>
        <stop offset="0.6" stop-color="var(--photo-mid)"/>
        <stop offset="1" stop-color="var(--photo-light)"/>
      </linearGradient>
    </defs>
    <polygon class="house-photo" role="img" aria-label="Photo of a modern two-storey house surrounded by trees on a pale backdrop"
      points="0,470 175,296 329,447 329,379 381,379 381,636 0,636" fill="url(#photoTone)"/>
    <polygon class="roof-line" fill="var(--bronze)"
      points="0,453 175,278 316,419 316,362 381,362 381,379 329,379 329,447 175,296 0,470"/>
  </svg>

  <h1 class="agent-name"><span class="agent-name__first">RAVI</span> <span class="agent-name__last">MENON</span></h1>
  <p class="agent-role">Real Estate Agent</p>

  <div class="contact-rail" aria-hidden="true">
    <svg class="contact-icon" style="top:5px" viewBox="0 0 24 24">
      <path fill="#fff" d="M6.6 10.8a15.1 15.1 0 0 0 6.6 6.6l2.2-2.2c.3-.3.7-.4 1-.2 1.1.4 2.3.6 3.6.6.6 0 1 .4 1 1V20c0 .6-.4 1-1 1A17 17 0 0 1 3 4c0-.6.4-1 1-1h3.5c.6 0 1 .4 1 1 0 1.2.2 2.4.6 3.6.1.3 0 .7-.2 1z"/>
    </svg>
    <svg class="contact-icon" style="top:30px" viewBox="0 0 24 24">
      <rect x="2" y="4" width="20" height="12" rx="1" fill="none" stroke="#fff" stroke-width="2.5"/>
      <rect x="10" y="16" width="4" height="3" fill="#fff"/>
      <rect x="7" y="19" width="10" height="2" fill="#fff"/>
    </svg>
    <svg class="contact-icon" style="top:54px" viewBox="0 0 24 24">
      <path fill="#fff" d="M12 2a7 7 0 0 0-7 7c0 5.2 7 13 7 13s7-7.8 7-13a7 7 0 0 0-7-7zm0 9.5A2.5 2.5 0 1 1 12 6.5a2.5 2.5 0 0 1 0 5z"/>
    </svg>
  </div>
  <ul class="contact-list">
    <li>+000 12345 6789</li>
    <li>www.yourwebsite.com</li>
    <li>Your street address-1234</li>
  </ul>

  <p class="brand-name">CREST</p>
</section>

<section class="card card--back" aria-label="Business card back">
  <svg class="card__shapes" viewBox="0 0 381 636" aria-hidden="true">
    <polygon class="house-block" fill="var(--bronze)"
      points="0,452 175,277 317,418 317,362 381,362 381,636 0,636"/>
  </svg>
  <p class="brand-name">CREST</p>
  <p class="tagline">Serving<br>your home<br>selling needs.</p>
</section>

</body>
</html>
```